Boutique Film/TV Company needs Business Card Design

Please see our website for background on our company and look of our current logo: www.lumarocpictures.ca

Pantone 314U is our main colour.

Target Market(s)

Network of peers, funders and broadcasters.

Industry/Entity Type

Business

Requirements
Must have
• We would like rounded corners and the height of the card to be shorter than traditional (maybe?!)

It's important that we have room for our office address, office number, cell number, email address, website, facebook and linked-in info (though not all of us have a linked-in account).

Would like the logo to keep the exclamation marks over the letters but the tag line/tag words of "film - television - interactive" can stay or go or... surprise me!

Nice to have
• Silky matte finish.

We are open to a change in the font of our logo/name.

```html
<!DOCTYPE html>
<html lang="en">
<head>
<meta charset="utf-8">
<title>Lumaroc Business Card</title>
<link rel="stylesheet" href="https://fonts.googleapis.com/css2?family=Source+Sans+3:wght@400;600;700&display=swap">
<style>
  :root {
    --backdrop: #ece7e1;
    --card: #ffffff;
    --card-edge: #d2cdc7;
    --brand: #9b1c24;
    --ink: #111111;
    --text: #444444;
    --social: #9b1c24;
  }
  html, body {
    margin: 0;
    padding: 0;
    width: 1200px;
    height: 1135px;
    overflow: hidden;
    background: var(--backdrop);
    font-family: "Source Sans 3", "Helvetica Neue", Arial, sans-serif;
  }
  .canvas {
    position: relative;
    width: 1200px;
    height: 1135px;
  }
  .card {
    position: absolute;
    width: 846px;
    height: 482px;
    background: var(--card);
    border-radius: 42px;
    border: 1px solid var(--card-edge);
    box-shadow: 0 2px 6px rgba(0,0,0,0.12);
    overflow: hidden;
  }
  .card--front { left: 58px; top: 52px; }
  .card--back  { left: 294px; top: 580px; }

  .wordmark {
    position: absolute;
    margin: 0;
    font-size: 118px;
    font-weight: 400;
    line-height: 1;
    color: var(--ink);
    letter-spacing: -1px;
  }
  .tagline {
    position: absolute;
    margin: 0;
    font-size: 23px;
    font-weight: 700;
    color: var(--brand);
    white-space: nowrap;
  }
  .card--front .wordmark { left: 108px; top: 66px; }
  .card--front .tagline  { left: 110px; top: 196px; }

  .contact-list {
    position: absolute;
    left: 0;
    top: 265px;
    margin: 0;
    padding: 0;
    list-style: none;
  }
  .contact-row {
    position: absolute;
    left: 0;
    display: flex;
    align-items: flex-start;
    white-space: nowrap;
  }
  .contact-row--address { top: 0; }
  .contact-row--phone   { top: 80px; }
  .contact-row--email   { top: 112px; }
  .contact-row--web     { top: 144px; }
  .contact-label {
    width: 95px;
    height: 23px;
    padding-right: 6px;
    box-sizing: border-box;
    background: var(--brand);
    color: #fff;
    font-size: 19px;
    line-height: 23px;
    text-align: right;
  }
  .contact-value {
    margin-left: 10px;
    font-size: 21px;
    line-height: 28px;
    margin-top: -3px;
    color: var(--text);
  }

  .follow {
    position: absolute;
    left: 599px;
    top: 395px;
    display: flex;
    align-items: center;
    gap: 10px;
  }
  .follow-label {
    font-size: 25px;
    font-weight: 700;
    color: var(--brand);
  }
  .social-icon { display: block; }

  .card--back .wordmark { left: 0; right: 0; top: 150px; text-align: center; }
  .card--back .tagline  { left: 0; right: 0; top: 268px; text-align: center; }
  .web-address {
    position: absolute;
    left: 0;
    right: 0;
    top: 375px;
    margin: 0;
    text-align: center;
    font-size: 30px;
    font-weight: 400;
    letter-spacing: 2px;
    color: var(--text);
  }
</style>
</head>
<body>
<main class="canvas">

  <section class="card card--front" aria-label="Business card front">
    <h1 class="wordmark">Lumaroc</h1>
    <p class="tagline">Films • Television • Interactive</p>

    <ul class="contact-list">
      <li class="contact-row contact-row--address">
        <span class="contact-label">Address</span>
        <span class="contact-value">Street Name, City Name<br>State, City Zip Code</span>
      </li>
      <li class="contact-row contact-row--phone">
        <span class="contact-label">Phone</span>
        <span class="contact-value">123-456-7890</span>
      </li>
      <li class="contact-row contact-row--email">
        <span class="contact-label">Email</span>
        <span class="contact-value">info@lumarocpictures.ca</span>
      </li>
      <li class="contact-row contact-row--web">
        <span class="contact-label">Web</span>
        <span class="contact-value">www.lumarocpictures.ca</span>
      </li>
    </ul>

    <div class="follow">
      <span class="follow-label">Follow us:</span>
      <svg class="social-icon" width="32" height="32" viewBox="0 0 32 32" aria-label="Professional network profile">
        <rect width="32" height="32" rx="4" fill="var(--social)"/>
      </svg>
      <svg class="social-icon" width="32" height="32" viewBox="0 0 32 32" aria-label="Social network page">
        <rect width="32" height="32" rx="4" fill="var(--social)"/>
      </svg>
    </div>
  </section>

  <section class="card card--back" aria-label="Business card back">
    <p class="wordmark">Lumaroc</p>
    <p class="tagline">Films • Television • Interactive</p>
    <p class="web-address">www.lumarocpictures.ca</p>
  </section>

</main>
</body>
</html>
```